High-End Residential and Commercial Appliance Repair Redesign (Winnipeg)

Full redesign and migration of https://tallpineappliancecare.ca from Divi to Kadence WP (Gutenberg).

Technical requirements:

Performance: Mobile PageSpeed Insights score must be 90+.

Framework: Use Kadence Theme and Kadence Blocks only. No heavy builders or extra plugins.

SEO: 1:1 migration of all existing URL slugs, H1-H3 headers, and meta-data.

Architecture: All styles must be managed via Kadence Customizer (Global Palette and Typography).

New pages and content expansion:
The designer must create new dedicated landing pages for the following services:

Commercial Reach-in Refrigeration: Prep tables and beverage coolers only. No walk-in units.

Commercial Dishwashers: Professional undercounter, hood-type, and conveyor units.

Commercial Laundry: High-capacity professional washers and dryers.

Commercial Electric Ovens: Professional ranges and convection ovens. No gas equipment.

Residential Brands: Individual pages for Frostline, Brann, Lumo, Tessa, and Halden.

Homepage structure:
The homepage must feature a dual-entry hero section to clearly separate Residential and Commercial clients.

Maintenance and handover:
The site must be built using professional standards for future maintenance by web developers. Documentation on site architecture is required upon completion.

Target Market(s)

Homeowners in Winnipeg seeking premium repair for luxury appliance brands (Frostline, Brann, Tessa), AND local business managers (restaurants, hotels, care homes) needing urgent repair for commercial electric kitchen and laundry equipment.

Industry/Entity Type

Appliance Repair Services

Coding

Coded - Design and coding required

Number of Pages Required

5+ page

Requirements
Must have
• Built strictly on Kadence WP Theme and Gutenberg Blocks. Mobile PageSpeed Insights score of 90+. Clear dual-entry homepage separating Residential and Commercial clients.
Nice to have
• Modular block design for easy future scaling. Premium visual aesthetic for luxury residential brands. Solid, highly professional B2B layout for commercial pages. Clear UI placeholders for future trust badges and company benefits.
Should not have
• Strictly NO AI-generated images and NO generic, cheap-looking stock photography. AI and standard free stock images look unnatural and destroy the premium, trustworthy standard of our brand. Use ONLY highly authentic, premium-grade imagery, or use clean placeholders (e.g., solid color blocks) where we will later insert the client's actual real-life photos.

```html
<!DOCTYPE html>
<html lang="en">
<head>
<meta charset="utf-8">
<title>Tall Pine Appliance Care – Luxury Appliance Repair in Winnipeg</title>
<link href="https://fonts.googleapis.com/css2?family=Outfit:wght@400;500;600;700;800&display=swap" rel="stylesheet">
<style>
:root{
  --red:#d0181d;
  --red-dark:#b51217;
  --blue:#2f5ba8;
  --blue-btn:#3564b4;
  --ink:#111111;
  --text:#4a4a4a;
  --muted:#777;
  --line:#d9d9d9;
  --soft:#f3f3f3;
  --white:#ffffff;
  --black:#0b0b0b;
}
*{box-sizing:border-box;margin:0;padding:0}
html,body{width:1200px;height:4762px;overflow:hidden}
body{font-family:'Outfit',sans-serif;color:var(--ink);background:var(--white);position:relative}
.abs{position:absolute}
.btn{display:inline-flex;align-items:center;justify-content:center;height:44px;padding:0 22px;border-radius:5px;color:var(--white);font-size:14px;font-weight:500;text-decoration:none}
.btn-red{background:var(--red)}
.btn-blue{background:var(--blue-btn)}
h2.section-title{font-size:33px;font-weight:700;text-align:center;letter-spacing:-.2px}
.photo{border-radius:10px}

/* header */
.site-header{top:0;left:0;width:1200px;height:107px}
.brand-block{left:0;top:0;width:350px;height:107px;background:var(--red);clip-path:polygon(0 0,100% 0,78% 100%,0 100%)}
.brand-name{left:112px;top:30px;color:var(--white);line-height:1}
.brand-name b{display:block;font-size:31px;font-weight:700;letter-spacing:.5px}
.brand-name span{display:block;font-size:16px;font-weight:400;letter-spacing:1.2px;margin-top:3px}
.topbar{left:340px;top:0;width:860px;height:37px;background:var(--black);clip-path:polygon(2% 0,100% 0,100% 100%,0 100%);display:flex;align-items:center;justify-content:flex-end;gap:58px;padding-right:112px;color:var(--white);font-size:12.5px}
.topbar .item{display:flex;align-items:center;gap:9px}
.main-nav{top:37px;right:112px;height:70px;display:flex;align-items:center;gap:60px;font-size:13px;color:#333}
.nav-call{display:flex;align-items:center;height:42px;background:var(--blue-btn);border-radius:4px;padding:3px 22px 3px 3px;color:var(--white);gap:16px;margin-left:-12px}
.nav-call i{width:36px;height:36px;background:var(--white);border-radius:3px;display:flex;align-items:center;justify-content:center}

/* hero */
.hero{top:107px;left:0;width:1200px;height:660px;background:linear-gradient(100deg,#2e2e2e 0%,#5a5a5a 45%,#8d8d8d 100%)}
.hero-photo{position:absolute;right:0;top:0;width:620px;height:660px;background:linear-gradient(160deg,#9a9a9a,#c7c7c7 55%,#8a8a8a)}
.hero-copy{position:absolute;left:115px;top:148px;color:var(--white)}
.hero-copy h1{font-size:51px;line-height:57px;font-weight:700;letter-spacing:-.3px}
.hero-copy .lead{font-size:13px;margin-top:20px}
.hero-copy .tick{display:flex;gap:8px;font-size:13px;line-height:19px;margin-top:14px;width:410px}
.hero-copy .ctas{display:flex;gap:12px;margin-top:22px}

/* services */
.services-title{top:850px;left:0;width:1200px}
.services-intro{top:905px;left:235px;width:730px;text-align:center;font-size:12.5px;line-height:19px;color:var(--text)}
.appliance-row{top:1004px;left:181px;display:flex;gap:13px}
.appliance{width:158px;text-align:center}
.appliance .card{height:170px;border-radius:10px;background:var(--white);box-shadow:0 2px 12px rgba(0,0,0,.12);display:flex;align-items:center;justify-content:center}
.appliance .card div{width:84px;height:104px;border-radius:6px;background:linear-gradient(180deg,#e9e9e9,#bdbdbd)}
.appliance p{font-size:14px;font-weight:600;margin-top:16px}

/* about */
.about-photo{top:1300px;left:185px;width:421px;height:362px;background:linear-gradient(135deg,#d8dde4,#f3f3f3 50%,#7a8fb8)}
.about-copy{top:1325px;left:655px;width:370px}
.about-copy h2{font-size:32px;line-height:42px;font-weight:700}
.about-copy p{font-size:12.5px;line-height:19px;color:var(--text);margin-top:16px}
.about-copy .btn{margin-top:24px}

/* service cards band */
.services-band{top:1784px;left:0;width:1200px;height:316px;background:var(--blue)}
.services-band h2{color:var(--white);position:absolute;top:70px;width:100%}
.service-cards{top:1928px;left:115px;display:flex;gap:17px}
.service-card{width:230px;height:280px;background:var(--white);border-radius:10px;box-shadow:0 3px 14px rgba(0,0,0,.12);overflow:hidden;text-align:center}
.service-card .ph{height:172px}
.service-card h3{font-size:14px;font-weight:600;margin-top:20px}
.service-card p{font-size:12px;line-height:18px;color:var(--text);margin:7px 22px 0}

/* brands */
.brands-title{top:2290px;left:0;width:1200px}
.brand-row{top:2354px;left:144px;display:flex;gap:10px}
.brand-tile{width:175px;height:55px;border-radius:4px;display:flex;align-items:center;justify-content:center;font-size:21px;font-weight:600}
.dots{display:flex;gap:9px;justify-content:center;width:1200px;left:0}
.dots i{width:9px;height:9px;border-radius:50%;background:#ddd}
.dots i.on{background:var(--red);width:11px;height:11px;margin-top:-1px}

/* why */
.why{top:2580px;left:153px;width:436px}
.why h2{font-size:32px;font-weight:700}
.why .point{border-bottom:1px solid #999;padding:18px 0 18px}
.why .point:last-child{border:none}
.why h3{font-size:14px;font-weight:600}
.why p{font-size:12px;line-height:18px;color:var(--text);margin-top:8px}
.why-photo{top:2557px;left:671px;width:376px;height:390px;background:linear-gradient(150deg,#f2f2f2,#cfd3da 55%,#3a4f7f)}

/* testimonials */
.testi-title{top:3038px;left:0;width:1200px}
.quote{top:3108px;left:572px}
.testi-text{top:3156px;left:215px;width:770px;text-align:center;font-size:17.5px;line-height:26px;color:#333}
.testi-name{top:3266px;left:0;width:1200px;text-align:center;font-size:14px;font-weight:600}
.stars{top:3292px;left:0;width:1200px;text-align:center;color:#f2b01e;font-size:15px;letter-spacing:1px}

/* contact band */
.contact-band{top:3448px;left:0;width:1200px;height:317px;background:var(--red)}
.contact-copy{position:absolute;left:113px;top:103px;width:440px;color:var(--white)}
.contact-copy h2{font-size:34px;font-weight:700}
.contact-copy p{font-size:12px;line-height:18.5px;margin-top:12px}
.contact-form{position:absolute;left:623px;top:48px;width:464px}
.field{background:var(--white);border-radius:5px;height:40px;font-size:11.5px;color:#777;padding:0 22px;display:flex;align-items:center;margin-bottom:8px}
.field-row{display:flex;gap:8px}
.field-row .field{flex:1}
.field.msg{height:82px;align-items:flex-start;padding-top:16px}
.submit{background:var(--blue-btn);height:40px;border-radius:5px;color:var(--white);font-size:12.5px;display:flex;align-items:center;justify-content:center;position:relative}
.submit svg{position:absolute;right:18px}

/* faq */
.faq-title{top:3855px;left:0;width:1200px}
.faq{top:3920px;left:268px;width:664px}
.faq-item{background:var(--soft);border-radius:4px;padding:17px 26px;margin-bottom:12px;position:relative}
.faq-item h3{font-size:13.5px;font-weight:600}
.faq-item p{font-size:11.5px;color:var(--text);margin-top:10px}
.faq-item svg{position:absolute;right:22px;top:22px}

/* cta */
.cta{top:4226px;left:0;width:1200px;text-align:center}
.cta h2{font-size:50px;font-weight:700;letter-spacing:-.3px}
.cta p{font-size:12.5px;line-height:19px;color:var(--text);width:730px;margin:6px auto 0}
.cta .btn{margin-top:26px;height:40px;font-size:12.5px}

/* footer */
.site-footer{top:4489px;left:0;width:1200px;height:273px;background:var(--black);color:var(--white)}
.footer-brand{position:absolute;left:113px;top:86px;line-height:1}
.footer-brand b{display:block;font-size:41px;font-weight:700;letter-spacing:.5px}
.footer-brand span{display:block;font-size:23px;letter-spacing:1.6px;margin-top:4px}
.footer-nav{position:absolute;right:112px;top:87px;display:flex;gap:44px;font-size:12px}
.footer-rule{position:absolute;left:684px;top:113px;width:404px;height:1px;background:#444}
.footer-contact{position:absolute;right:112px;top:129px;display:flex;gap:100px;font-size:12px}
.footer-contact .item{display:flex;gap:8px;align-items:center}
.copyright{position:absolute;bottom:26px;width:100%;text-align:center;font-size:11.5px}
.chat-bubble{right:38px;bottom:46px;width:42px;height:42px;border-radius:50%;background:#25c15b}
</style>
</head>
<body>

<header class="site-header abs">
  <div class="brand-block abs"></div>
  <div class="brand-name abs"><b>TALL PINE</b><span>APPLIANCE CARE</span></div>
  <div class="topbar abs">
    <span class="item"><svg width="12" height="12" viewBox="0 0 24 24"><path fill="#e02a2a" d="M6.6 10.8a15 15 0 006.6 6.6l2.2-2.2c.3-.3.7-.4 1-.2 1.1.4 2.3.6 3.6.6.6 0 1 .4 1 1V20c0 .6-.4 1-1 1A17 17 0 013 4c0-.6.4-1 1-1h3.5c.6 0 1 .4 1 1 0 1.3.2 2.5.6 3.6.1.3 0 .7-.2 1z"/></svg>431-555-0147</span>
    <span class="item"><svg width="13" height="11" viewBox="0 0 24 18"><rect width="24" height="18" rx="2" fill="#e02a2a"/><path d="M1 2l11 8 11-8" stroke="#0b0b0b" stroke-width="2" fill="none"/></svg>hello@tallpinecare.ca</span>
    <span class="item"><svg width="11" height="14" viewBox="0 0 20 26"><path fill="#e02a2a" d="M10 0a10 10 0 00-10 10c0 7 10 16 10 16s10-9 10-16A10 10 0 0010 0zm0 14a4 4 0 110-8 4 4 0 010 8z"/></svg>18 Birchwood Bay, Winnipeg, MB R2C 4K1, Canada</span>
  </div>
  <nav class="main-nav abs">
    <span>Services</span><span>Brands</span><span>Reviews</span><span>Blog</span><span>Contact Us</span>
    <span class="nav-call"><i><svg width="16" height="16" viewBox="0 0 24 24"><path fill="#d0181d" d="M6.6 10.8a15 15 0 006.6 6.6l2.2-2.2c.3-.3.7-.4 1-.2 1.1.4 2.3.6 3.6.6.6 0 1 .4 1 1V20c0 .6-.4 1-1 1A17 17 0 013 4c0-.6.4-1 1-1h3.5c.6 0 1 .4 1 1 0 1.3.2 2.5.6 3.6.1.3 0 .7-.2 1z"/></svg></i>431-555-0147</span>
  </nav>
</header>

<section class="hero abs">
  <div class="hero-photo" role="img" aria-label="Technician in red cap and overalls kneeling to repair a front-load washing machine"></div>
  <div class="hero-copy">
    <h1>Luxury Residential<br>Appliance Repair<br>in Winnipeg</h1>
    <p class="lead">Premium service for Frostline, Brann, Tessa and other high-end brands.</p>
    <div class="tick"><svg width="13" height="13" viewBox="0 0 24 24" style="flex:none;margin-top:3px"><circle cx="12" cy="12" r="12" fill="#fff"/><path d="M6.5 12.5l3.5 3.5 7.5-8" stroke="#333" stroke-width="2.6" fill="none"/></svg><span>Commercial Kitchen &amp; Laundry Equipment Repair Fast response for restaurants, hotels &amp; care facilities.</span></div>
    <div class="ctas"><a class="btn btn-red">Residential Service</a><a class="btn btn-blue">Commercial Service</a></div>
  </div>
</section>

<h2 class="section-title services-title abs">Your One-Stop Appliance Services</h2>
<p class="services-intro abs">With a decade of dedicated experience, Tall Pine Appliance Care delivers reliable and professional repairs for commercial and residential appliances. Our seasoned technicians specialize in fixing appliances from any brand and offer a three-month warranty on all repairs. We prioritize customer satisfaction with budget-friendly prices and provide same-day service for your convenience. Choose Tall Pine Appliance Care for trusted expertise.</p>
<div class="appliance-row abs">
  <div class="appliance"><div class="card"><div role="img" aria-label="Washer"></div></div><p>Washer</p></div>
  <div class="appliance"><div class="card"><div role="img" aria-label="Dryer"></div></div><p>Dryer</p></div>
  <div class="appliance"><div class="card"><div role="img" aria-label="Refrigerator" style="width:60px;height:116px"></div></div><p>Refrigerator</p></div>
  <div class="appliance"><div class="card"><div role="img" aria-label="Oven and stove" style="width:78px;height:86px"></div></div><p>Oven &amp; Stove</p></div>
  <div class="appliance"><div class="card"><div role="img" aria-label="Dishwasher" style="width:80px;height:108px"></div></div><p>Dishwasher</p></div>
</div>

<div class="about-photo photo abs" role="img" aria-label="Technician in blue overalls servicing a washing machine"></div>
<div class="about-copy abs">
  <h2>Appliance Repair<br>And Maintenance in<br>Winnipeg</h2>
  <p>Welcome to Tall Pine Appliance Care – your go-to for fast, reliable, and budget-friendly appliance repairs. Trusted by your neighbours, we fix any brand with a three-month warranty. Enjoy same-day service for your convenience. Choose Tall Pine Appliance Care–your reliable company for any type of appliance repair and maintenance.</p>
  <a class="btn btn-red">Request a Repair</a>
</div>

<section class="services-band abs">
  <h2 class="section-title">Our Appliance Repair Services</h2>
</section>
<div class="service-cards abs">
  <div class="service-card"><div class="ph" role="img" aria-label="Technician servicing a commercial dishwasher" style="background:linear-gradient(160deg,#c9c9c9,#8b8b8b)"></div><h3>Commercial Dishwashers</h3><p>Professional undercounter, hood type.</p></div>
  <div class="service-card"><div class="ph" role="img" aria-label="Person holding folded towels in a laundry room" style="background:linear-gradient(160deg,#e6e6e6,#a7b2bf)"></div><h3>Commercial Laundry</h3><p>High-capacity professional washers and dryers.</p></div>
  <div class="service-card"><div class="ph" role="img" aria-label="Chef working at a commercial electric oven" style="background:linear-gradient(160deg,#4a4a4a,#1e1e1e)"></div><h3>Commercial Electric Ovens</h3><p>Professional ranges &amp; convection ovens. No gas equipment.</p></div>
  <div class="service-card"><div class="ph" role="img" aria-label="Residential home exterior with open house sign" style="background:linear-gradient(160deg,#c8d3c0,#7f8f78)"></div><h3>Residential Brands</h3><p>Individual pages for Frostline, Brann, Lumo, Tessa &amp; Halden.</p></div>
</div>

<h2 class="section-title brands-title abs">Brands we repair</h2>
<div class="brand-row abs">
  <div class="brand-tile" style="background:#ececec">Kestrel</div>
  <div class="brand-tile" style="background:#fbe6ea">Norvane</div>
  <div class="brand-tile" style="background:#e9edf5">Elvara</div>
  <div class="brand-tile" style="background:#f8f1dc">Swirlmax</div>
  <div class="brand-tile" style="background:#ececec">Ardell</div>
</div>
<div class="dots abs" style="top:2450px"><i></i><i class="on"></i><i></i></div>

<div class="why abs">
  <h2>Why Choose Us?</h2>
  <div class="point" style="padding-top:22px"><h3>Repair on the Same Day</h3><p>At Tall Pine Appliance Care, we understand the urgency of getting your appliances back in action. Our commitment to prompt service ensures that we offer same-day repairs to minimize disruptions in your daily routine.</p></div>
  <div class="point"><h3>Satisfaction Guaranteed</h3><p>Our skilled technicians are dedicated to delivering top-notch appliance repairs, ensuring that your devices function optimally.</p></div>
  <div class="point"><h3>10 Year Experience</h3><p>Over the past decade, we've successfully resolved a myriad of appliance issues, earning the trust of our valued customers.</p></div>
</div>
<div class="why-photo photo abs" role="img" aria-label="Two technicians lifting a washing machine"></div>

<h2 class="section-title testi-title abs">Our Testimonials</h2>
<svg class="quote abs" width="56" height="44" viewBox="0 0 56 44"><path fill="#d0181d" d="M0 44V26C0 12 7 3 21 0l2 6C15 9 12 14 12 20h11v24zm33 0V26C33 12 40 3 54 0l2 6c-8 3-11 8-11 14h11v24z"/></svg>
<p class="testi-text abs">Tall Pine Appliance Care technician Marco exhibited friendliness and profound knowledge while assessing my washing machine. He inquired extensively to grasp the nature of the issue. His thorough approach left me confident that the issue was resolved, and he also provided valuable advice. I plan to reach out to Tall Pine Appliance Care again.</p>
<p class="testi-name abs">Daniel Reyes</p>
<p class="stars abs">★★★★★</p>
<div class="dots abs" style="top:3342px"><i></i><i class="on"></i><i></i></div>

<section class="contact-band abs">
  <div class="contact-copy">
    <h2>Call or Email Us Today</h2>
    <p>Connect with us today to explore how our expertise can help you with your repair needs. Connect with us today to explore how our expertise can help you with your repair needs. Call at 431-555-0147 or fill out the form below and describe the problem you have.</p>
  </div>
  <div class="contact-form">
    <div class="field-row"><div class="field">Enter Your Name....</div><div class="field">Enter Your Phone....</div></div>
    <div class="field">Enter Your Email Address....</div>
    <div class="field msg">Please Send Your Message....</div>
    <div class="submit">Submit Now<svg width="16" height="16" viewBox="0 0 24 24"><path fill="#fff" d="M2 11L22 2l-9 20-2-8z"/></svg></div>
  </div>
</section>

<h2 class="section-title faq-title abs">Frequently Asked Questions</h2>
<div class="faq abs">
  <div class="faq-item"><h3>Why do I need to pay for a service call (diagnostics)?</h3><p>This involves contacting a technician to visit the site and conduct on-site diagnostics.</p><svg width="10" height="6" viewBox="0 0 10 6"><path d="M1 1l4 4 4-4" stroke="#333" stroke-width="1.5" fill="none"/></svg></div>
  <div class="faq-item"><h3>How much warranty do I have for a replaced part?</h3><svg width="10" height="6" viewBox="0 0 10 6" style="top:20px"><path d="M1 5l4-4 4 4" stroke="#333" stroke-width="1.5" fill="none"/></svg></div>
  <div class="faq-item"><h3>If a customer proceeds with the repair, does he need to pay for diagnostics?</h3><svg width="10" height="6" viewBox="0 0 10 6" style="top:20px"><path d="M1 5l4-4 4 4" stroke="#333" stroke-width="1.5" fill="none"/></svg></div>
</div>

<section class="cta abs">
  <h2>We are Available 24/7!</h2>
  <p>Do you have questions about your appliances or need professional repair services? We're here to assist you. Use the information below to contact Tall Pine Appliance Care or call us today—your satisfaction is our priority.</p>
  <a class="btn btn-red">Contact Us Today</a>
</section>

<footer class="site-footer abs">
  <div class="footer-brand"><b>TALL PINE</b><span>APPLIANCE CARE</span></div>
  <nav class="footer-nav"><span>Services</span><span>Brands</span><span>Reviews</span><span>Blog</span><span>Contact Us</span></nav>
  <div class="footer-rule"></div>
  <div class="footer-contact">
    <span class="item"><svg width="11" height="11" viewBox="0 0 24 24"><path fill="#fff" d="M6.6 10.8a15 15 0 006.6 6.6l2.2-2.2c.3-.3.7-.4 1-.2 1.1.4 2.3.6 3.6.6.6 0 1 .4 1 1V20c0 .6-.4 1-1 1A17 17 0 013 4c0-.6.4-1 1-1h3.5c.6 0 1 .4 1 1 0 1.3.2 2.5.6 3.6.1.3 0 .7-.2 1z"/></svg>Call Us: 431-555-0147</span>
    <span class="item"><svg width="12" height="10" viewBox="0 0 24 18"><rect width="24" height="18" rx="2" fill="#fff"/><path d="M1 2l11 8 11-8" stroke="#0b0b0b" stroke-width="2" fill="none"/></svg>Email: hello@tallpinecare.ca</span>
  </div>
  <p class="copyright">Tall Pine Appliance Care 2026 | Privacy Policy</p>
</footer>
<div class="chat-bubble abs" aria-label="Chat"></div>

</body>
</html>
```